Professional Mothers Wordpress Site

*** To be clear, as a result of this contest I am looking for a fully functioning wordpress site to import into my wordpress site. Not just an image layout design.***

A Responsive Wordpress Blog Site for Professional Mothers

List of features desired:
1. Social media platform and commenting
2. Fully featured ecommerce store
3. Create and display fantastic-looking galleries of vimeo video content
4. Customised slideshows that are displayed in a content slider. Slides can be filled with text, images, video, social media stream feeds and syndicated content like Chirpline feeds, YouTube, Pinterest, Flickr and more.
5. HTML5 and Flash compatible audio player that sits within the site. Works across both desktop and mobile devices
6. Admin panel
7. Google docs integrated email subscription, forms etc., email opt-in for newsletter
8. URL shortener
9. Enhanced image gallery
10. Interactive drag-and-drop pricing tables
11. Google Analytics, sitemaps
12. Rating system

List of pages on blogsite
1. Home page
2. About page
3. Resources page
4. Podcast archive page
5. Coaching page
6. Contact page

Here are some things I liked about the blogs I clicked through (and why I did or didn't like them)

Examples:
1) http://www.brindlecove.com/‎ - clean, professional feel
2) http://www.tessagrundvik.com/ - i like the simplicity of the email sign up and how it stands out without being obnoxious
3) http://clovertrailworks.com/ - i like the simplicity of the links to various pages at the top
4) http://www.velmarstudio.com/ - i like how the links are clear at the top and how they stay still even if the page moves (persistent headers)
5) http://www.hustlepanorama.com/ - i like how the podcast sessions are laid out on the front page
6) http://www.quorvane.com/ - this has a really nice 1st impression
7) http://dadwanderbook.com/ - this has a nice layout too but the logo is way too big and it takes too long to scroll down to the content
8) http://tiltbix.com/ - I like the moving content of this

Overall I'm going for something neat, clean and simple.

Target Market(s)

Mothercrest

Industry/Entity Type

Store

Requirements
Must have
• The social media links at the top of the page

```html
<!DOCTYPE html>
<html lang="en">
<head>
<meta charset="utf-8">
<title>Mothercrest</title>
<link href="https://fonts.googleapis.com/css2?family=Arimo:wght@400;700&family=Oswald:wght@500;600&display=swap" rel="stylesheet">
<style>
:root{
  --page:#f1f1f1;
  --paper:#ffffff;
  --ink:#2a2a2a;
  --muted:#6b6b6b;
  --nav:#151515;
  --purple:#5a2570;
  --purple-deep:#3c1250;
  --magenta:#b8197f;
  --red:#d5322b;
  --blue:#2c7fc3;
  --band:#3a3d33;
  --rule:#dcdcdc;
}
*{box-sizing:border-box;margin:0;padding:0}
html,body{width:813px;height:1200px;overflow:hidden}
body{background:var(--page);font-family:"Arimo",Arial,sans-serif;color:var(--ink);position:relative}
.page{position:absolute;left:58px;top:0;width:697px;height:1111px;background:var(--paper)}
.abs{position:absolute}

/* header */
.brand{left:12px;top:10px;display:flex;align-items:center;gap:8px}
.brand-dot{width:16px;height:16px;border-radius:50%;background:var(--magenta)}
.brand-name{font-size:22px;font-weight:700;color:var(--purple)}
.account{right:12px;top:12px;font-size:9px;font-weight:700;color:var(--ink);letter-spacing:.3px}
.account .sep{color:var(--muted);margin:0 5px}
.account .reg{color:var(--magenta)}
.social{display:flex;gap:3px}
.social span{width:13px;height:13px;display:block}
.s-purple{background:var(--purple)}.s-red{background:var(--red)}.s-blue{background:var(--blue)}
.head-social{right:12px;top:31px}

.main-nav{left:10px;top:57px;width:677px;height:18px;background:var(--nav);display:flex;align-items:center;padding-left:10px;gap:16px}
.main-nav a{color:#fff;font-size:7.5px;font-weight:700;text-decoration:none;letter-spacing:.3px}

/* slider */
.slider{left:10px;top:75px;width:677px;height:290px;background:linear-gradient(100deg,#28351d 0%,#4f6b34 30%,#8aa36a 55%,#c9b8a4 72%,#5e86b0 90%,#35597f 100%)}
.slider-title{left:36px;top:60px;font-family:"Oswald",Arial,sans-serif;font-weight:600;color:#fff;font-size:27px;line-height:1.08;letter-spacing:.5px}
.arrow{top:130px;width:22px;height:22px;border-radius:50%;background:rgba(0,0,0,.55)}
.arrow svg{display:block}
.arrow.prev{left:8px}.arrow.next{right:8px}

/* signup band */
.tips{left:10px;top:365px;width:677px;height:46px;background:linear-gradient(180deg,#464a3e,var(--band));display:flex;align-items:center;padding:0 14px;gap:10px}
.tips-label{color:#fff;font-size:11.5px;font-weight:700;letter-spacing:.2px;flex:1}
.tips input{width:104px;height:18px;border:0;background:#fff;font-family:inherit;font-size:7px;padding-left:5px;color:var(--muted)}
.tips button{width:44px;height:18px;border:0;background:var(--purple-deep);color:#fff;font-family:inherit;font-size:7.5px;font-weight:700}

/* videos */
.section-head{font-size:8px;font-weight:700;color:var(--muted);letter-spacing:.3px}
.section-head b{color:var(--purple)}
.videos-head{left:10px;top:424px}
.video{top:440px;width:214px;height:112px;overflow:hidden}
.video .cap{position:absolute;left:0;bottom:0;width:100%;height:17px;background:rgba(20,20,20,.85);color:#e04fb0;font-size:7.5px;font-weight:700;padding:5px 8px}
.v1{left:10px;background:linear-gradient(135deg,#c9d7e2,#8fb0c6 60%,#d8c3b1)}
.v2{left:241px;background:linear-gradient(135deg,#b9c9a0,#7f9c5b 50%,#cdb495)}
.v3{left:472px;background:linear-gradient(135deg,#bdbdbd,#6e6e6e 55%,#3d3d3d)}

/* articles */
.article h2{font-size:10px;font-weight:700;line-height:1.25;color:var(--ink);width:488px}
.meta{font-size:6.5px;color:var(--purple);font-weight:700;margin-top:3px}
.txt{font-size:6.3px;line-height:1.45;color:var(--muted)}
.more{color:var(--purple);font-weight:700}
.share{display:flex;gap:3px}
.share span{width:11px;height:11px;display:block}
.a1{left:10px;top:583px}
.photo{background:linear-gradient(135deg,#9fc0d9,#d2433a 45%,#e8e2da 80%)}
.photo2{background:linear-gradient(180deg,#1d2a55,#6c4f83 45%,#d58352 70%,#1e1e2a)}
.rule{height:1px;background:var(--rule)}

/* sidebar */
.side{left:510px;width:177px}
.chirp-head{display:flex;align-items:center;gap:5px}
.chirp-dot{width:12px;height:12px;background:var(--blue)}
.chirp-name{font-size:17px;font-weight:700;color:var(--blue)}
.chirp-feeds{font-size:8px;font-weight:700;color:var(--ink)}
.tweet{display:flex;gap:6px;margin-top:8px}
.avatar{width:30px;height:30px;flex:none;background:linear-gradient(135deg,#c6a89a,#6b5a66)}
.gallery{display:grid;grid-template-columns:repeat(3,55px);gap:5px}
.gallery div{height:50px}
.g1{background:linear-gradient(135deg,#d8c2b0,#8a6d60)}
.g2{background:linear-gradient(135deg,#b5c7d6,#667f95)}
.g3{background:linear-gradient(135deg,#e5d4c5,#a47d6b)}
.g4{background:linear-gradient(135deg,#a9b98f,#5d6e48)}
.g5{background:linear-gradient(135deg,#d9b7ae,#94625a)}
.g6{background:linear-gradient(135deg,#c9c3ba,#75706a)}
.g7{background:linear-gradient(135deg,#bfcfdc,#7d8f9f)}
.g8{background:linear-gradient(135deg,#e2cbb8,#b28c73)}
.g9{background:linear-gradient(135deg,#b4a79c,#62574f)}

/* footer */
.footer{left:0;top:1111px;width:813px;height:89px;background:linear-gradient(180deg,var(--purple),var(--purple-deep))}
.foot-nav{left:68px;top:14px;display:flex;gap:14px}
.foot-nav a{color:#fff;font-size:7px;font-weight:700;text-decoration:none}
.foot-social{right:68px;top:11px}
.foot-social span{width:12px;height:12px}
.copy{left:68px;top:34px;font-size:6.5px;color:#d9c6e2;line-height:1.5}
</style>
</head>
<body>
<div class="page">
  <div class="abs brand"><span class="brand-dot"></span><span class="brand-name">Mothercrest</span></div>
  <div class="abs account">MY CART<span class="sep">|</span>LOGIN<span class="sep">|</span><span class="reg">REGISTER</span></div>
  <div class="abs social head-social"><span class="s-purple"></span><span class="s-red"></span><span class="s-blue"></span></div>

  <nav class="abs main-nav">
    <a href="#">HOME</a><a href="#">ABOUT US</a><a href="#">SERVICES</a><a href="#">ARTICLES</a><a href="#">GALLERY</a><a href="#">VIDEOS</a><a href="#">SHOP</a><a href="#">SUPPORT</a><a href="#">CONTACT US</a>
  </nav>

  <section class="abs slider" role="img" aria-label="Slide photo of a smiling mother holding her baby outdoors">
    <h1 class="abs slider-title">THIS IS A CHARITY<br>FOUNDATION WEBSITE</h1>
    <span class="abs arrow prev"><svg width="22" height="22"><path d="M13 6 L8 11 L13 16" stroke="#fff" stroke-width="2.2" fill="none"/></svg></span>
    <span class="abs arrow next"><svg width="22" height="22"><path d="M9 6 L14 11 L9 16" stroke="#fff" stroke-width="2.2" fill="none"/></svg></span>
  </section>

  <section class="abs tips">
    <svg width="22" height="16" viewBox="0 0 22 16"><rect x="1" y="1" width="20" height="14" fill="none" stroke="#fff" stroke-width="1.5"/><path d="M1 1 L11 9 L21 1" fill="none" stroke="#fff" stroke-width="1.5"/></svg>
    <span class="tips-label">GET FREE TIPS, NEWSLETTERS &amp; SPECIAL OFFERS</span>
    <input type="text" placeholder="FIRST NAME">
    <input type="text" placeholder="EMAIL ADDRESS">
    <button>SIGN UP</button>
  </section>

  <div class="abs section-head videos-head">OUR VIDEOS &nbsp;|&nbsp; <b>VIEW ALL »</b></div>
  <div class="abs video v1" role="img" aria-label="Video still of a mother with her child"><div class="cap">MOTHERS LOVE</div></div>
  <div class="abs video v2" role="img" aria-label="Video still of a father with his son">
    <span class="abs arrow prev" style="top:40px;width:16px;height:16px"><svg width="16" height="16"><path d="M10 4 L6 8 L10 12" stroke="#fff" stroke-width="2" fill="none"/></svg></span>
    <span class="abs arrow next" style="top:40px;width:16px;height:16px"><svg width="16" height="16"><path d="M6 4 L10 8 L6 12" stroke="#fff" stroke-width="2" fill="none"/></svg></span>
    <div class="cap">LOVE FATHER LOVE SON</div></div>
  <div class="abs video v3" role="img" aria-label="Black and white video still of a family"><div class="cap">LOREM IPSUM DIOS</div></div>

  <article class="abs article a1">
    <h2>PROIN VEL LACINIA IPSUM. DONEC FACILISIS DUI QUIS ELIT TEMPOR ALIQUET. CURABITUR ID ORCI TURPIS</h2>
    <div class="meta">POSTED BY: ADMIN &nbsp; ON: 9.1.13</div>
    <div style="display:flex;gap:10px;margin-top:6px">
      <div class="photo" style="width:200px;height:118px;flex:none" role="img" aria-label="Photo of a group of children in red shirts"></div>
      <p class="txt" style="width:278px">Proin vel lacinia ipsum. Donec facilisis dui quis elit tempor aliquet. Curabitur id orci turpis, ac ultricies nulla. Cras enim ligula, blandit elementum placerat sed, vehicula ac orci. Nunc in ligula ac est hendrerit aliquet sed a mi. Mauris at ligula ex.<br><br>Proin vel lacinia ipsum. Donec facilisis dui quis elit tempor aliquet. Curabitur id orci turpis, ac ultricies nulla. Cras enim ligula, blandit elementum placerat sed, vehicula ac orci. Nunc in ligula ac est hendrerit aliquet.</p>
    </div>
    <p class="txt" style="width:488px;margin-top:8px">Proin vel lacinia ipsum. Donec facilisis dui quis elit tempor aliquet. Curabitur id orci turpis, ac ultricies nulla. Cras enim ligula, blandit elementum placerat sed, vehicula ac orci. Nunc in ligula ac est hendrerit aliquet sed a mi. Mauris at ligula ex. <span class="more">Read full story</span></p>
    <div class="share" style="margin-top:7px"><span class="s-purple"></span><span class="s-red"></span><span class="s-blue"></span></div>
    <div class="rule" style="width:488px;margin-top:14px"></div>

    <h2 style="margin-top:14px">PROIN VEL LACINIA IPSUM. DONEC FACILISIS DUI QUIS ELIT TEMPOR ALIQUET. CURABITUR ID ORCI TURPIS</h2>
    <div class="meta">POSTED BY: ADMIN &nbsp; ON: 9.1.13</div>
    <div style="display:flex;gap:10px;margin-top:6px">
      <div class="photo2" style="width:200px;height:122px;flex:none" role="img" aria-label="Photo of a starry evening sky over a landscape"></div>
      <p class="txt" style="width:278px">Proin vel lacinia ipsum. Donec facilisis dui quis elit tempor aliquet. Curabitur id orci turpis, ac ultricies nulla. Cras enim ligula, blandit elementum placerat sed, vehicula ac orci. Nunc in ligula ac est hendrerit aliquet sed a mi. Mauris at ligula ex.<br><br>Proin vel lacinia ipsum. Donec facilisis dui quis elit tempor aliquet. Curabitur id orci turpis, ac ultricies nulla. Cras enim ligula, blandit elementum placerat sed, vehicula ac orci.</p>
    </div>
    <p class="txt" style="width:488px;margin-top:8px">Proin vel lacinia ipsum. Donec facilisis dui quis elit tempor aliquet. Curabitur id orci turpis, ac ultricies nulla. Cras enim ligula, blandit elementum placerat sed, vehicula ac orci. Nunc in ligula ac est hendrerit aliquet sed a mi. <span class="more">Read full story</span></p>
    <div class="share" style="margin-top:7px"><span class="s-purple"></span><span class="s-red"></span><span class="s-blue"></span></div>
  </article>

  <aside class="abs side" style="top:583px">
    <div class="chirp-head"><span class="chirp-dot"></span><span class="chirp-name">Chirpline</span><span class="chirp-feeds">FEEDS</span></div>
    <div class="tweet"><div class="avatar" role="img" aria-label="Profile photo"></div><p class="txt">Proin vel lacinia ipsum. Donec facilisis dui quis elit tempor aliquet. Curabitur id orci turpis.</p></div>
    <div class="tweet"><div class="avatar" role="img" aria-label="Profile photo"></div><p class="txt">Curabitur id orci turpis, ac ultricies nulla. Cras enim ligula, blandit sed, vehicula ac orci.</p></div>
    <p class="txt more" style="margin-top:5px">More feeds</p>
    <div class="rule" style="margin:10px 0"></div>
    <div class="section-head" style="font-size:10px;color:var(--ink);margin-bottom:8px">PHOTO GALLERY</div>
    <div class="gallery" role="img" aria-label="Grid of family and mother photos">
      <div class="g1"></div><div class="g2"></div><div class="g3"></div>
      <div class="g4"></div><div class="g5"></div><div class="g6"></div>
      <div class="g7"></div><div class="g8"></div><div class="g9"></div>
    </div>
  </aside>
</div>

<footer class="abs footer">
  <nav class="abs foot-nav"><a href="#">HOME</a><a href="#">ABOUT US</a><a href="#">SERVICES</a><a href="#">ARTICLES</a><a href="#">GALLERY</a><a href="#">VIDEOS</a><a href="#">SHOP</a><a href="#">SUPPORT</a><a href="#">CONTACT US</a></nav>
  <div class="abs social foot-social"><span class="s-purple" style="background:#7a3f93"></span><span class="s-red"></span><span class="s-blue"></span></div>
  <p class="abs copy">COPYRIGHT 2013, ALL RIGHTS RESERVED<br>TERMS &amp; CONDITIONS &nbsp;|&nbsp; PRIVACY &nbsp;|&nbsp; DISCLAIMER</p>
</footer>
</body>
</html>
```